Business Card Design Project

I am a Chiropractor that is looking for a new business card.  Our logo was slightly changed lately, therefore need a new, more professional look.
We are a modern, non-stuffy chiropractic office.  Want a contemporary look that will let people know this is not your typical doctors office.  Our logo is red, and contains the name of our business: realign.  The u in the logo is green, stressing the most important part of our business: "u"

Target Market(s)
moderate to upper income bracket, family friendly
www.realignspine-example.com
Gordon Pell
Family Chiropractor
314 Hollis Rd
Harlow Creek, NM 87999
512.555.0147 phone
512.555.0148 fax
Industry/Entity Type
Business
Requirements
Must have
- www.realignspine-example.com
Gordon Pell
Family Chiropractor
314 Hollis Rd
Harlow Creek, NM 87999
512.555.0147 phone
512.555.0148 fax

```html
<!DOCTYPE html>
<html lang="en">
<head>
<meta charset="utf-8">
<title>realign — Business Card</title>
<link href="https://fonts.googleapis.com/css2?family=Didact+Gothic&display=swap" rel="stylesheet">
<style>
  :root {
    --brand-red: #ee4137;
    --brand-green: #5aa846;
    --paper: #ffffff;
    --backdrop: #ece9e4;
    --ink-white: #ffffff;
  }
  * { box-sizing: border-box; margin: 0; padding: 0; }
  html, body {
    width: 1200px; height: 900px; overflow: hidden;
    background: var(--backdrop);
    font-family: "Didact Gothic", "Century Gothic", sans-serif;
  }
  .canvas {
    width: 1200px; height: 900px;
    display: flex; align-items: center; justify-content: center; gap: 60px;
  }
  .card {
    width: 525px; height: 300px;
    position: relative; overflow: hidden;
    box-shadow: 0 10px 28px rgba(0,0,0,.18);
  }

  /* Front */
  .card--front {
    background: var(--brand-red);
    display: flex; flex-direction: column; align-items: center; justify-content: center;
    color: var(--ink-white);
  }
  .front__name { font-size: 104px; line-height: 1; letter-spacing: 1px; }
  .front__web { margin-top: 14px; font-size: 15px; letter-spacing: 4px; }

  /* Back */
  .card--back { background: var(--paper); display: flex; flex-direction: column; }
  .back__brand {
    height: 44%;
    display: flex; align-items: center; justify-content: center; gap: 14px;
  }
  .back__brand-dot { width: 18px; height: 18px; border-radius: 50%; background: var(--brand-green); }
  .back__brand-name { font-size: 56px; line-height: 1; color: var(--brand-red); }
  .back__rule { height: 3px; background: var(--brand-green); }
  .back__details {
    flex: 1; background: var(--brand-red); color: var(--ink-white);
    display: flex; align-items: center; padding: 0 30px 0 34px;
  }
  .person { flex: 1; }
  .person__name { font-size: 30px; line-height: 1.1; }
  .person__title { font-size: 15px; margin-top: 4px; }
  .divider { width: 1px; align-self: stretch; margin: 28px 24px; background: rgba(255,255,255,.55); }
  .contact { list-style: none; font-size: 13.5px; line-height: 1.45; white-space: nowrap; }
  .contact__row { display: flex; align-items: flex-start; gap: 9px; }
  .contact__icon {
    width: 14px; height: 14px; margin-top: 2px; flex: none;
    background: var(--paper); border-radius: 2px;
    display: flex; align-items: center; justify-content: center;
  }
  .contact__icon svg { width: 10px; height: 10px; }
  .contact__spacer { height: 6px; }
</style>
</head>
<body>
<main class="canvas">

  <section class="card card--front" aria-label="Card front">
    <div class="front__name">realign</div>
    <div class="front__web">www.realignspine-example.com</div>
  </section>

  <section class="card card--back" aria-label="Card back">
    <div class="back__brand">
      <span class="back__brand-dot"></span>
      <span class="back__brand-name">realign</span>
    </div>
    <div class="back__rule"></div>
    <div class="back__details">
      <div class="person">
        <div class="person__name">Gordon Pell</div>
        <div class="person__title">Family Chiropractor</div>
      </div>
      <div class="divider"></div>
      <ul class="contact">
        <li class="contact__row">
          <span class="contact__icon"><svg viewBox="0 0 10 10"><path d="M5 0.5a3 3 0 0 0-3 3c0 2.3 3 6 3 6s3-3.7 3-6a3 3 0 0 0-3-3z" fill="#5aa846"/><circle cx="5" cy="3.5" r="1.1" fill="#fff"/></svg></span>
          <span>314 Hollis Rd<br>Harlow Creek, NM 87999</span>
        </li>
        <li class="contact__spacer"></li>
        <li class="contact__row">
          <span class="contact__icon"><svg viewBox="0 0 10 10"><path d="M2.2 1l1.6 2-1 1c.6 1.3 1.6 2.3 2.9 2.9l1-1 2 1.6-.9 1.5C4.5 8.8 1.2 5.5 1 1.9z" fill="#5aa846"/></svg></span>
          <span>512.555.0147</span>
        </li>
        <li class="contact__row">
          <span class="contact__icon"><svg viewBox="0 0 10 10"><rect x="1" y="4" width="8" height="5" rx="1" fill="#5aa846"/><rect x="2.5" y="1" width="5" height="3.5" fill="none" stroke="#5aa846" stroke-width="1"/></svg></span>
          <span>512.555.0148</span>
        </li>
        <li class="contact__row">
          <span class="contact__icon"><svg viewBox="0 0 10 10"><circle cx="5" cy="5" r="4" fill="none" stroke="#5aa846" stroke-width="1"/><path d="M1 5h8M5 1c-2 2.5-2 5.5 0 8M5 1c2 2.5 2 5.5 0 8" fill="none" stroke="#5aa846" stroke-width=".8"/></svg></span>
          <span>www.realignspine-example.com</span>
        </li>
      </ul>
    </div>
  </section>

</main>
</body>
</html>
```